Quorvix Letter head

Quorvix is a young and energetic software development consultancy. We spend our time working with clients to turn what ever is in their heads in to software.
We are trying to create an image of a high class software boutique who build class leading bespoke solutions.
We need a sharp letter head that looks great on high quality media.
We like bold colours and distinctive design. So show us what you can do.
Industry/Entity Type
Software
Requirements
Must have
- Our company is based in the UK and are requried to have on the paper somewhere the following information:
* Registered company name: Quorvix Ltd
* Registered company number
* VAT registration number
In addition we also want the following:
* An email address
* Telephone number
* Website address
An example of what some pages have in their footer is something like the following:
Quorvix Ltd is registered in England and Wales. Reg. no: 5316274
Registered office: 48 Cobblewick Road, Harlow Essex, CM93TP. Tel: 07712365081
You do not have to use this sentance but please make sure your design incorporates accommodates the requirements for UK based companies

```html
<!DOCTYPE html>
<html lang="en">
<head>
<meta charset="utf-8">
<title>Quorvix Letterhead</title>
<link rel="stylesheet" href="https://fonts.googleapis.com/css2?family=Open+Sans:wght@400&display=swap">
<style>
  :root {
    --backdrop: #e9e7e4;
    --paper: #ffffff;
    --brand-red: #c42030;
    --brand-red-light: #dc2a37;
    --brand-red-dark: #b01a26;
    --ink-grey: #a3a5a8;
    --rule-grey: #9b9d9f;
    --footer-rule: #b9bbbd;
    --footer-text: #ffffff;
  }
  * { margin: 0; padding: 0; box-sizing: border-box; }
  html, body {
    width: 1140px;
    height: 1200px;
    overflow: hidden;
    background: var(--backdrop);
    font-family: "Open Sans", Arial, sans-serif;
  }
  .letterhead {
    position: absolute;
    left: 156px;
    top: 17px;
    width: 828px;
    height: 1165px;
    background: var(--paper);
    box-shadow: 0 2px 10px rgba(0, 0, 0, 0.12);
  }
  .brand-name {
    position: absolute;
    left: 27px;
    top: 8px;
    font-size: 80px;
    line-height: 1;
    font-weight: 400;
    letter-spacing: 1px;
    color: var(--brand-red);
  }
  .contact-block {
    position: absolute;
    left: 589px;
    top: 19px;
    padding-left: 12px;
    border-left: 2px solid var(--rule-grey);
    font-style: normal;
    font-size: 16px;
    line-height: 21.6px;
    color: var(--ink-grey);
    letter-spacing: 0.2px;
    white-space: nowrap;
  }
  .footer-band {
    position: absolute;
    left: 0;
    right: 0;
    bottom: 0;
    height: 56px;
    border-top: 3px solid var(--footer-rule);
    background: linear-gradient(to bottom, var(--brand-red-light), var(--brand-red-dark));
    display: flex;
    flex-direction: column;
    align-items: center;
    justify-content: center;
    gap: 2px;
  }
  .registration-note {
    font-size: 13.5px;
    line-height: 18px;
    color: var(--footer-text);
    letter-spacing: 0.2px;
    white-space: nowrap;
  }
</style>
</head>
<body>
  <main class="letterhead">
    <header>
      <div class="brand-name">QUORVIX</div>
      <address class="contact-block">
        48 Cobblewick Road,<br>
        Harlow Essex, CM93TP<br>
        T:07712365081<br>
        E:hello@quorvix.co.uk<br>
        W:www.quorvix.co.uk
      </address>
    </header>
    <footer class="footer-band">
      <p class="registration-note">Quorvix Ltd is registered in England and Wales. Reg. no: 5316274</p>
      <p class="registration-note">VAT Reg. no: GB 284 6193 57</p>
    </footer>
  </main>
</body>
</html>
```